Sticker label for natural moisturizer

I need a sticker label designed for a homemade moisturizer made from beef tallow and honey.
Must include: Logo, product name (Classic Suet & Clover Salve), ingredients (in English and Polish, can use placeholder text for initial design), brief description of product with instructions for use (in English and Polish, can use placeholder text for initial design), manufacturer name (vorelmart.com), manufacturer address (placeholder text for initial design), volume of container (60ml / 2oz)
The product is used by both males and females of all ages, so must be unisex design with broad appeal.
Dimensions: Length 15cm, Height 3cm
Style: Has to simultaneously communicate that this is a homemade product with no chemical fillers AND that it is of extremely high quality.
Brand colors:
#57665C
#FCFAF6
#FFFFFF
#000000
#B99B83
#EAE4DD
#CC8E5A

```html
<!DOCTYPE html>
<html lang="en">
<head>
<meta charset="utf-8">
<title>vorel – Classic Suet &amp; Clover Salve label</title>
<link href="https://fonts.googleapis.com/css2?family=Fraunces:opsz,wght@9..144,600;9..144,700&family=Hind:wght@400;500;600&display=swap" rel="stylesheet">
<style>
  :root {
    --sage: #57665C;
    --sage-light: #6a796f;
    --cream: #FCFAF6;
    --white: #FFFFFF;
    --stone: #EAE4DD;
    --clay: #CC8E5A;
    --clay-dark: #a8703f;
  }
  * { margin: 0; padding: 0; box-sizing: border-box; }
  html, body {
    width: 1200px; height: 1014px; overflow: hidden;
    background: var(--white);
    font-family: "Hind", sans-serif;
  }
  .label {
    position: absolute; left: 30px; top: 103px;
    width: 1132px; height: 227px;
    background: var(--white);
  }
  .top-band {
    position: absolute; left: 0; top: 0; width: 100%; height: 105px;
    background: var(--sage);
    color: var(--cream);
  }
  .bottom-band {
    position: absolute; left: 0; top: 111px; width: 100%; height: 116px;
    background: var(--clay);
  }
  .ingredients {
    position: absolute; left: 20px; top: 14px; width: 340px;
    font-size: 8.6px; line-height: 9.2px; font-weight: 500;
  }
  .ingredients p + p { margin-top: 9px; }
  .ingredients b, .usage b { font-weight: 600; }
  .brand-name {
    position: absolute; left: 430px; top: -6px; width: 330px;
    text-align: center;
    font-family: "Fraunces", serif; font-weight: 600;
    font-size: 88px; line-height: 110px; letter-spacing: 1px;
    color: var(--stone);
  }
  .usage {
    position: absolute; left: 801px; top: 30px; width: 315px;
    font-size: 8.6px; line-height: 9.2px; font-weight: 500;
  }
  .usage p + p { margin-top: 9px; }
  .claims { position: absolute; left: 67px; top: 22px; width: 270px; height: 56px; }
  .artwork {
    position: absolute; left: 368px; top: 6px; width: 140px; height: 80px;
    border-radius: 40px 40px 12px 12px;
    background: linear-gradient(160deg, #c07f4c, #b8784a);
  }
  .product-name {
    position: absolute; left: 470px; top: 9px; width: 287px;
    text-align: right;
    font-family: "Fraunces", serif; font-weight: 600;
    font-size: 31px; line-height: 31px;
    color: var(--sage);
  }
  .volume {
    position: absolute; left: 517px; top: 86px; width: 98px; height: 22px;
    background: var(--white); color: var(--clay);
    font-size: 15px; line-height: 24px; text-align: center; font-weight: 500;
  }
  .maker {
    position: absolute; left: 843px; top: 30px; width: 230px; height: 46px;
    border: 1.5px solid var(--white); border-radius: 8px;
    color: var(--white); text-align: center;
  }
  .maker-title {
    position: absolute; left: 50%; top: -8px; transform: translateX(-50%);
    background: var(--clay); padding: 0 8px;
    font-size: 11px; line-height: 14px; font-weight: 600; white-space: nowrap;
  }
  .maker-site { margin-top: 6px; font-size: 14px; line-height: 17px; font-weight: 600; }
  .maker-address { font-size: 11px; line-height: 14px; font-weight: 500; }
</style>
</head>
<body>
  <section class="label">
    <div class="top-band">
      <div class="ingredients">
        <p><b>Ingredients:</b> 100% Grass-fed Beef Tallow (Tallow), Cold Pressed Extra-virgin Olive Oil (Olea Europaea Fruit Oil), Beeswax (Cera Alba), Raw Honey (Mel), Essential oils of Bergamot (Citrus Bergamia) and Blood Orange (Citrus Sinensis)</p>
        <p><b>Skladniki:</b> 100% lóju wolowego (Tallow), oliwa z oliwek Extra Virgin tloczona na zimno (Olea Europaea Fruit Oil), wosk pszczeli (Cera Alba), miód z pasieki (Mel), olejki eteryczne z bergamotki (Citrus Bergamia) i czerwonej pomaranczy (Citrus Sinensis)</p>
      </div>
      <div class="brand-name">vorel</div>
      <div class="usage">
        <p><b>How to use:</b> Take a small amount and gently rub it into clean skin wherever you feel the need (anywhere works!)</p>
        <p><b>Sposób uzycia:</b> Nabierz niewielka ilosc i delikatnie wmasuj w czysta skóre, kiedy tylko poczujesz taka potrzebe (dziala na wszystkie partie ciala!</p>
      </div>
    </div>

    <div class="bottom-band">
      <svg class="claims" viewBox="0 0 270 56" aria-hidden="true">
        <rect x="1" y="3" width="36" height="48" rx="4" fill="#FFFFFF"/>
        <rect x="59" y="3" width="36" height="48" rx="4" fill="#FFFFFF"/>
        <circle cx="137" cy="27" r="23" fill="#FFFFFF"/>
        <circle cx="205" cy="27" r="25" fill="none" stroke="#FFFFFF" stroke-width="2"/>
        <circle cx="205" cy="27" r="19" fill="none" stroke="#FFFFFF" stroke-width="1.5"/>
      </svg>
      <div class="artwork" role="img" aria-label="Engraved sketch of a bowl of balm, a cloth-wrapped honey jar and honeycomb"></div>
      <div class="product-name">Classic Suet &amp;<br>Clover Salve</div>
      <div class="volume">60ml / 2oz</div>
      <div class="maker">
        <span class="maker-title">Manufactured by:</span>
        <div class="maker-site">vorelmart.com</div>
        <div class="maker-address">Lipowa 14C Krakow, 30-702 Polska</div>
      </div>
    </div>
  </section>
</body>
</html>
```